New Business Cards / Logo update

Logo:
can be updated but wanted pricing

New Business Cards:
take our existing business cards and upgrade them from a design perspective. We have two versions
Inside sales team does not have a cell phone and they use an appointment back slot.
Outside project managers and leadership uses a slogan backing and will have cell phones.

```html
<!DOCTYPE html>
<html lang="en">
<head>
<meta charset="utf-8">
<title>Harbor Carpet + Flooring – Business Cards</title>
<link href="https://fonts.googleapis.com/css2?family=EB+Garamond:ital,wght@0,400;0,500;1,400&display=swap" rel="stylesheet">
<style>
  :root {
    --bg: #2e2e2e;
    --card: #ffffff;
    --orange: #e08c22;
    --taupe: #938984;
    --ink: #333333;
    --faint: #e4e4e4;
    --white: #ffffff;
  }
  * { box-sizing: border-box; margin: 0; padding: 0; }
  html, body { width: 1200px; height: 875px; overflow: hidden; }
  body {
    background: var(--bg);
    font-family: "EB Garamond", Georgia, serif;
    display: flex;
    align-items: center;
    justify-content: center;
    gap: 40px;
  }
  .card {
    position: relative;
    width: 540px;
    height: 310px;
    background: var(--card);
    border-radius: 18px;
    overflow: hidden;
  }

  /* Appointment back */
  .appointment .tagline {
    position: absolute;
    left: 48px;
    top: 38px;
    color: var(--orange);
    font-style: italic;
    font-size: 40px;
    line-height: 1.02;
  }
  .appointment .tagline .lead { font-style: normal; font-weight: 500; }
  .appointment .band {
    position: absolute;
    left: 70px;
    top: 148px;
    width: 420px;
    height: 30px;
    border-radius: 15px;
    background: var(--taupe);
    color: var(--white);
    font-size: 15px;
    letter-spacing: 0.55em;
    display: flex;
    align-items: center;
    justify-content: center;
  }
  .appointment .slot-line {
    position: absolute;
    left: 48px;
    right: 48px;
    top: 208px;
    display: flex;
    align-items: flex-end;
    gap: 6px;
    font-size: 15px;
    color: var(--ink);
  }
  .appointment .dots {
    flex: 1;
    border-bottom: 1.5px dotted var(--ink);
    margin-bottom: 4px;
  }
  .appointment .web {
    position: absolute;
    left: 0;
    right: 0;
    top: 250px;
    text-align: center;
    color: var(--orange);
    font-size: 15px;
    letter-spacing: 0.03em;
  }

  /* Front */
  .front .art { position: absolute; inset: 0; }
  .front .wordmark {
    position: absolute;
    right: 30px;
    top: 42px;
    width: 190px;
    text-align: center;
    color: var(--orange);
    font-size: 28px;
    line-height: 1.1;
  }
  .front .slogan-art {
    position: absolute;
    right: 26px;
    bottom: 30px;
    width: 200px;
    height: 70px;
    border-radius: 35px;
    background: var(--faint);
    opacity: 0.7;
  }
  .front .contact {
    position: absolute;
    left: 34px;
    top: 112px;
    color: var(--white);
  }
  .front .name {
    font-size: 25px;
    font-weight: 500;
    letter-spacing: 0.04em;
    line-height: 1;
  }
  .front .role {
    font-style: italic;
    font-size: 16px;
    margin-top: 4px;
  }
  .front .details {
    list-style: none;
    margin-top: 12px;
    font-size: 14px;
    line-height: 1.35;
  }
  .front .details li {
    display: flex;
    align-items: flex-start;
    gap: 8px;
  }
  .front .details svg {
    width: 11px;
    height: 11px;
    margin-top: 4px;
    flex: none;
  }
  .front .details .spaced { margin-top: 6px; }
</style>
</head>
<body>

  <section class="card appointment">
    <p class="tagline"><span class="lead">Quality</span> flooring at<br>an affordable price.</p>
    <div class="band">APPOINTMENT</div>
    <div class="slot-line">
      <span>Date:</span><span class="dots"></span>
      <span>Time:</span><span class="dots"></span>
    </div>
    <p class="web">www.harborfloorsoutlet.com</p>
  </section>

  <section class="card front">
    <svg class="art" viewBox="0 0 540 310" aria-hidden="true">
      <circle cx="150" cy="262" r="222" fill="var(--orange)"/>
      <path d="M 262 18 A 262 262 0 0 1 402 232" fill="none" stroke="var(--orange)" stroke-width="4" stroke-linecap="round"/>
    </svg>

    <div class="wordmark">Harbor Carpet<br>+ Flooring</div>
    <div class="slogan-art" role="img" aria-label="Faint script slogan lettering"></div>

    <div class="contact">
      <h1 class="name">DANA WHITFIELD</h1>
      <p class="role">Sales + Design Manager</p>
      <ul class="details">
        <li>
          <svg viewBox="0 0 12 12"><path d="M6 0.5a4 4 0 0 0-4 4c0 3 4 7 4 7s4-4 4-7a4 4 0 0 0-4-4zm0 5.5a1.5 1.5 0 1 1 0-3 1.5 1.5 0 0 1 0 3z" fill="var(--white)"/></svg>
          <span>1520 Bayview Rd<br>Port Laurel, FL 34000</span>
        </li>
        <li class="spaced">
          <svg viewBox="0 0 12 12"><path d="M2.5 1l2 2-1 1.5c.6 1.5 1.5 2.4 3 3l1.5-1 2 2-1.5 1.5C5 10 2 7 1 2.5z" fill="var(--white)"/></svg>
          <span>555-014-2287</span>
        </li>
        <li>
          <svg viewBox="0 0 12 12"><rect x="0.5" y="2" width="11" height="8" fill="var(--white)"/><path d="M0.5 2l5.5 4.5L11.5 2" fill="none" stroke="var(--orange)" stroke-width="1"/></svg>
          <span>dana@harborfloorsoutlet.com</span>
        </li>
        <li>
          <svg viewBox="0 0 12 12"><circle cx="6" cy="6" r="5" fill="none" stroke="var(--white)" stroke-width="1.4"/><path d="M1 6h10M6 1c-2 2.5-2 7.5 0 10M6 1c2 2.5 2 7.5 0 10" fill="none" stroke="var(--white)" stroke-width="1"/></svg>
          <span>harborfloorsoutlet.com</span>
        </li>
      </ul>
    </div>
  </section>

</body>
</html>
```